Designing a "Yummy Mummy" Style Blog

I am clueless when it comes to technology and web design. I am starting a blog on pregnancy, babies and high society life in London. It's going to be called "Fizzwicks on Marlow", and will aim to be frank, funny and aspire to a certain type of luxury lifestyle.

I would like a well designed, sophisticated looking blog set up for me. I've never had a blog designed for me online before, so i am not entirely sure how it works but ideally i would like the whole "look set up" so i can get the password, add a domain to it and start inputting my text and pictures.

Basically i looked into setting up one myself on pagecraft/scribbleup.example but i realised that with my very basic know how, what i was going to end up with from the "template suggestions" was going to be pretty generic and i really want something unique and special as i am going to try and promote this alongside my writing career.

I would like a relatively non-fussy layout but the "Fizzwicks on Marlow" title i thought could be designed to look like a bit of a logo, with perhaps a cocktail on one end and a dummy/rattle on the other. I want the whole website to look fashionable, stylish and endorse a "yummy mummy lifestyle".

Ideally it would be very easy for me to upload text and pictures to the blog and it would be very visually appealing to look at and easy to read. It will need to have a list of all my blog posts on the side (obviously which are yet to be written, but the capability to have them all in the readers eye-line when they are eventually written!)

I would like to blog to look more like a website than a standard blog. See www.dapperpavement.example or www.vogrenstrand.example for the type of non-standard blog format i like.

Each post is going to be mainly text but then i would like the ability to add photos to each one. I also want the text spread across the page so that it becomes "about the writing"... what i mean is some blogs have lots of little tabs of text you can click on... i want my blog to scroll down so you read it like a story... a bit like www.bumpandbloomdiary.example or www.penvaleposts.example.

Look forward to seeing what you come up with. as an example of my personal style, please see my website www.roseharwick.example which was a clothing brand i designed a few years ago. See that i had an illustration of myself done (in the about section) i like the idea of some little drawings or something unique to make it original. Many thanks for your work in advance.

Please note, i have only made this work "refundable" because i havent done a web design style job post like this before and obviously have no idea whether this is something that would work (have someone design it online for me" BUT i fully intend to buy a design off here and am very serious about doing so so please know that if your design fits what i am looking for i am definitely buying it, this is a genuine committed request!

Many thanks
Updates

Reason: I am extending the deadline as i have just decided to Guarantee the prize money for the project. My email address is rose@roseharwick.example if you would like to email me any ideas/designs for the blog. Please know that i would like the actual blog set up for me on either pagecraft or scribbleup.example site under FIZZWICKS ON MARLOW (my new blog name). Obviously i will be buying the domain name for this but whoever comes up with the best design i will go onto whichever blog site you recommend, add register the FIZZWICKS ON MARLOW BLOG and then you can do all the design for me. Then you will be guaranteed payment on this site. So just know - whoever describes and shows me through logos, fonts and description the best design for my blog will be the one to do it! And i definitely will be choosing someone! Hope my main description give you enough to work out what kind of a style i want. Very modern, femine, fresh fun and clear but not TACKY.. no gaudy colours or pictures.. i want it to look like a glossy magazine column. THANKS x

Target Market(s)

Target market are trendy london girls and new mothers and mothers-to-be. It should appeal to feminine stylish, educated women.

Industry/Entity Type

Clothing

Requirements
Must have
• It must be set up as a blog on an easy to naviagate blog site that i can have easy access to update with my text and pictures using a password and username. It should also be able to have a domain added to it so i can buy www.inkspillsonmarlow.example if i so wish in the future.

INK SPILLS ON MARLOW the title should be designed to look like a logo and be bold and stand out.

The Font needs to be clear yet stylish. I do not want it to be an "all uppercase" font. I am a writer, so i need the ability to use lowercase and uppercase lettering !

Please make it look very clean and clear cut so the reader knows exactly what shes looking at. Some blogs just look too messy, you dont know what you are meant to be reading.

I want the blog to make it clear what the latest blog post is and have that at the top then have all the other blog posts in an archive style list to the left or right of the page. Please make the font clear enough to read but not too huge.

I am sure this goes without saying, but Please note this blog MUST be completely suitable for the UK. I would like it on a UK blog site, or one that is completely worldwide and works for the UK. (ie if this blog is successful i want to make sure i can promote it/advertise on it with uk brands etc)

```html
<!DOCTYPE html>
<html lang="en">
<head>
<meta charset="utf-8">
<title>Ink Spills on Marlow — Blog</title>
<link rel="stylesheet" href="https://fonts.googleapis.com/css2?family=Gelasio:wght@400;700&family=Source+Sans+3:wght@400;600;700&display=swap">
<style>
  :root {
    --page-bg: #f4f3f0;
    --card-bg: #ffffff;
    --card-border: #d9d8d4;
    --body-text: #3b3b3b;
    --accent-red: #b3121b;
    --pager-red: #e2283b;
    --pager-grey: #b3b3b3;
    --pager-text: #6d6d6d;
    --footer-bg: #2e2e2e;
    --footer-bg-dark: #262626;
    --footer-teal: #2aa3b5;
    --footer-heading: #d42a3c;
    --footer-rule-gold: #a07a2c;
    --footer-link: #9a9a9a;
    --footer-dash: #6a6a6a;
    --share-bg: #f1f0ec;
    --share-border: #d3d1cb;
    --share-text: #555555;
  }
  * { box-sizing: border-box; margin: 0; padding: 0; }
  html, body { width: 1200px; height: 900px; overflow: hidden; }
  body { position: relative; background: var(--page-bg); font-family: "Gelasio", Georgia, serif; }

  .post-card {
    position: absolute; left: 61px; top: -10px; width: 829px; height: 446px;
    background: var(--card-bg); border: 2px solid var(--card-border);
  }
  .post-shadow { position: absolute; left: 61px; top: 434px; width: 829px; height: 14px; }

  .post-body {
    position: absolute; left: 111px; top: -6px; width: 740px;
    font-size: 14px; line-height: 24px; letter-spacing: -0.05px; color: var(--body-text);
  }
  .post-body .line { display: block; white-space: nowrap; }
  .post-body .indent { padding-left: 36px; }
  .post-body .gap { height: 24px; display: block; }

  .read-more {
    position: absolute; left: 111px; top: 332px;
    font-size: 14.5px; font-weight: 700; color: var(--accent-red); text-decoration: none;
  }

  .share-bar {
    position: absolute; left: 412px; top: 368px; width: 275px; height: 30px; display: flex;
    border: 1px solid var(--share-border); border-radius: 3px; background: var(--share-bg);
    font-family: "Source Sans 3", Arial, sans-serif; font-size: 12.5px; color: var(--share-text);
  }
  .share-bar .share-item {
    display: flex; align-items: center; justify-content: center; gap: 4px; flex: auto;
    border-right: 1px solid var(--share-border);
  }
  .share-bar .share-item:last-child { border-right: 0; }
  .share-bar .dot { width: 6px; height: 6px; background: #8a8a8a; border-radius: 50%; }

  .pager { position: absolute; top: 458px; left: 0; width: 1200px; height: 40px;
    font-family: "Source Sans 3", Arial, sans-serif; font-size: 15px; color: var(--pager-text); }
  .pager .page { position: absolute; top: 0; text-align: center; }
  .pager .page::after { content: ""; position: absolute; left: 0; right: 0; top: 31px; height: 4px; background: var(--pager-grey); }
  .pager .page.current { color: #222; font-weight: 700; }
  .pager .page.current::after { background: var(--pager-red); }

  .site-footer {
    position: absolute; left: 0; top: 561px; width: 1200px; height: 339px;
    background: radial-gradient(ellipse at 50% 30%, var(--footer-bg) 0, var(--footer-bg-dark) 100%);
    border-top: 3px solid var(--footer-teal);
    font-family: "Source Sans 3", Arial, sans-serif;
  }
  .site-footer .stitch { position: absolute; left: 0; right: 0; top: 14px; border-top: 1px dashed #555; }

  .widget-title {
    position: absolute; top: 46px; font-size: 15px; font-weight: 700;
    color: var(--footer-heading); letter-spacing: 0.1px; line-height: 18px;
  }
  .widget-rule { position: absolute; height: 1px; background: var(--footer-heading); }
  .widget-rule.gold { background: var(--footer-rule-gold); }

  .footer-link { position: absolute; font-size: 12.5px; color: var(--footer-link); line-height: 16px; }
  .category-link { padding-bottom: 14px; border-bottom: 1px dashed var(--footer-dash); }

  .thumb {
    position: absolute; width: 83px; height: 83px; border: 3px solid #fafafa;
    box-shadow: 0 0 0 1px #888;
  }
</style>
</head>
<body>

  <div class="post-card"></div>
  <svg class="post-shadow" viewBox="0 0 829 14" preserveAspectRatio="none" aria-hidden="true">
    <path d="M0 0 H829 C700 3 560 8 414 8 C268 8 128 3 0 0Z" fill="#d9d8d3"/>
  </svg>

  <article class="post-body">
    <span class="line">quarta decima et quinta decima. Eodem modo typi, qui nunc nobis videntur parum clari, fiant sollemnes in futurum.</span>
    <span class="gap"></span>
    <span class="line indent">Lorem ipsum dolor sit amet, consectetuer adipiscing elit, sed diam nonummy nibh euismod tincidunt ut laoreet</span>
    <span class="line">dolore magna aliquam erat volutpat. Ut wisi enim ad minim veniam, quis nostrud exerci tation ullamcorper suscipit</span>
    <span class="line">lobortis nisl ut aliquip ex ea commodo consequat. Duis autem vel eum iriure dolor in hendrerit in vulputate velit esse</span>
    <span class="line">molestie consequat, vel illum dolore eu feugiat nulla facilisis at vero eros et accumsan et iusto odio dignissim qui blan-</span>
    <span class="line">dit praesent luptatum zzril delenit augue duis dolore te feugait nulla facilisi. Nam liber tempor cum soluta nobis eleif-</span>
    <span class="line">end option congue nihil imperdiet doming id quod mazim placerat facer possim assum. Typi non habent claritatem</span>
    <span class="line">insitam; est usus legentis in iis qui facit eorum claritatem. Investigationes demonstraverunt lectores legere me lius</span>
    <span class="line">quod ii legunt saepius.</span>
    <span class="line indent">Claritas est etiam processus dynamicus, qui sequitur mutationem consuetudium lectorum. Mirum est notare</span>
    <span class="line">quam littera gothica, quam nunc putamus parum claram, anteposuerit litterarum formas humanitatis per seacula</span>
    <span class="line">quarta decima et quinta decima. Eodem modo typi, qui nunc nobis videntur parum clari, fiant sollemnes in futurum.</span>
  </article>

  <a class="read-more" href="#">Read more...</a>

  <div class="share-bar">
    <span class="share-item"><span class="dot"></span>Facefolio</span>
    <span class="share-item"><span class="dot"></span>Chirpline</span>
    <span class="share-item"><span class="dot"></span>Searchly</span>
    <span class="share-item"><span class="dot"></span>Pinbox</span>
  </div>

  <nav class="pager">
    <span class="page current" style="left:330px;width:30px">1</span>
    <span class="page" style="left:366px;width:30px">2</span>
    <span class="page" style="left:402px;width:30px">3</span>
    <span class="page" style="left:437px;width:30px">4</span>
    <span class="page" style="left:474px;width:30px">5</span>
    <span class="page" style="left:510px;width:30px">6</span>
    <span class="page" style="left:548px;width:35px">&gt;&gt;</span>
    <span class="page" style="left:589px;width:43px">Last</span>
  </nav>

  <footer class="site-footer">
    <div class="stitch"></div>

    <h3 class="widget-title" style="left:129px">CATEGORIES</h3>
    <span class="widget-rule gold" style="left:241px;top:56px;width:108px"></span>
    <span class="footer-link category-link" style="left:130px;top:92px;width:96px">Streets</span>
    <span class="footer-link category-link" style="left:250px;top:92px;width:96px">Social Media</span>
    <span class="footer-link category-link" style="left:130px;top:140px;width:96px">Fashion</span>
    <span class="footer-link category-link" style="left:250px;top:140px;width:102px">Entertainment</span>
    <span class="footer-link" style="left:130px;top:188px">Magazine</span>

    <h3 class="widget-title" style="left:409px;top:47px">ARCHIVES</h3>
    <span class="widget-rule" style="left:505px;top:57px;width:125px"></span>
    <span class="footer-link" style="left:410px;top:93px">September 2012</span>
    <span class="footer-link" style="left:410px;top:122px">July 2012</span>
    <span class="footer-link" style="left:410px;top:151px">June 2012</span>
    <span class="footer-link" style="left:410px;top:180px">May 2012</span>
    <span class="footer-link" style="left:410px;top:209px">April 2012</span>

    <h3 class="widget-title" style="left:687px;top:47px">SNAPSTREAM</h3>
    <span class="widget-rule" style="left:800px;top:57px;width:108px"></span>
    <div class="thumb" role="img" aria-label="Black and white ink illustration with lettering" style="left:690px;top:97px;background:#c9c9c9"></div>
    <div class="thumb" role="img" aria-label="Illustrated horned creature in brown tones" style="left:787px;top:97px;background:linear-gradient(#a9b7ad,#7a4a33)"></div>
    <div class="thumb" role="img" aria-label="Photo of a band playing in warm stage light" style="left:882px;top:97px;background:linear-gradient(135deg,#3a2a1e,#a8782f)"></div>
    <div class="thumb" role="img" aria-label="Black and white ink lettering artwork" style="left:690px;top:193px;background:#bdbdbd"></div>
    <div class="thumb" role="img" aria-label="Collage artwork in teal and green tones" style="left:787px;top:193px;background:linear-gradient(#7fa9a3,#2f5b3a)"></div>
    <div class="thumb" role="img" aria-label="Full moon behind bare tree silhouettes" style="left:884px;top:193px;background:radial-gradient(circle at 55% 40%,#e8ebee 0,#b9c1c8 35%,#14191e 70%)"></div>
  </footer>

</body>
</html>
```